University Student Business Card

Looking for a professional university student business card. Student is studying business with a focus on marketing. Some combination using a monogram and/or full name on the front with full name, university details and contact information on the back. Card should be modern design for a young professional. Prefer use of royal blue, black and white but am open to other uses of colour palette if it reinforces young/trendy style. Initials for a monogram are: KM. Full details will be provided in private consultation with designer(s).

Target Market(s)

Professional business people, marketers, advertisers, consultants

Industry/Entity Type

Business, marketing

Contact Information for Business Card

Monogram or personal logo, full name, university name, program of study, phone number, email address, linkedin address

Other font styles liked:
• Open to suggestion to fulfill above requirements

Colors
0054AA
0677BA
7BADD7
CADEEF
E8F1F8

Requirements
Must have
• Monogram using letters K and M, and incorporate the business card details listed in the brief (specific details including personal contact info will be shared with successful designer to ensure privacy)
Nice to have
• Personal brand using monogram or personal logo (not a business logo)

```html
<!DOCTYPE html>
<html lang="en">
<head>
<meta charset="utf-8">
<title>KM Student Business Card</title>
<link href="https://fonts.googleapis.com/css2?family=Open+Sans:wght@400;600;700&display=swap" rel="stylesheet">
<style>
  :root {
    --royal: #2d3a92;
    --ink: #27348b;
    --paper: #f3f3f3;
    --stage: #262626;
    --white: #ffffff;
  }
  * { margin: 0; padding: 0; box-sizing: border-box; }
  html, body {
    width: 1200px; height: 1000px; overflow: hidden;
    background: var(--stage);
    font-family: "Open Sans", sans-serif;
  }
  .canvas { position: relative; width: 1200px; height: 1000px; }
  .card {
    position: absolute;
    width: 479px; height: 283px;
    border-radius: 21px;
    left: 373px;
  }
  .card-front { top: 170px; background: var(--royal); }
  .card-back { top: 550px; background: var(--paper); color: var(--ink); }

  .monogram {
    position: absolute;
    transform: translate(-50%, -50%);
    font-weight: 700;
    letter-spacing: -2px;
    line-height: 1;
  }
  .card-front .monogram { left: 240px; top: 142px; font-size: 66px; color: var(--white); }
  .card-back .monogram { left: 358px; top: 140px; font-size: 66px; color: var(--ink); }

  .holder-name {
    position: absolute; left: 45px; top: 74px;
    font-size: 17.5px; font-weight: 400; color: var(--ink);
  }
  .contact-list {
    position: absolute; left: 45px; top: 117px;
    list-style: none;
  }
  .contact-item {
    display: flex; align-items: center;
    height: 22px;
    font-size: 12.5px; color: var(--ink);
  }
  .contact-icon {
    width: 14px; height: 14px; margin-right: 8px;
    flex: none;
  }
  .divider {
    position: absolute; left: 239px; top: 44px;
    width: 1.5px; height: 195px; background: var(--ink);
  }
  .social-row {
    position: absolute; left: 382px; top: 246px;
    display: flex; gap: 4px;
  }
  .social-dot {
    width: 14px; height: 14px; border-radius: 50%;
    background: var(--ink);
  }
</style>
</head>
<body>
<main class="canvas">
  <section class="card card-front" aria-label="Card front">
    <div class="monogram">KM</div>
  </section>

  <section class="card card-back" aria-label="Card back">
    <h1 class="holder-name">your name</h1>
    <ul class="contact-list">
      <li class="contact-item">
        <svg class="contact-icon" viewBox="0 0 14 14"><rect width="14" height="14" rx="2" fill="#27348b"/><path d="M4.5 3.2 L6 3 L6.6 5.2 L5.6 6 Q6.5 8 8 8.6 L8.9 7.6 L11 8.3 L10.8 9.8 Q7.5 10.5 5 7.6 Q3.6 5.5 4.5 3.2Z" fill="#fff"/></svg>
        (555)014-2287
      </li>
      <li class="contact-item">
        <svg class="contact-icon" viewBox="0 0 14 14"><rect width="14" height="14" rx="2" fill="#27348b"/><rect x="2.5" y="4" width="9" height="6.5" fill="none" stroke="#fff" stroke-width="1.1"/><path d="M2.5 4 L7 7.6 L11.5 4" fill="none" stroke="#fff" stroke-width="1.1"/></svg>
        youremail@mailbox.com
      </li>
      <li class="contact-item">
        <svg class="contact-icon" viewBox="0 0 14 14"><rect width="14" height="14" rx="2" fill="#27348b"/><circle cx="7" cy="7" r="4.3" fill="none" stroke="#fff" stroke-width="0.9"/><ellipse cx="7" cy="7" rx="1.8" ry="4.3" fill="none" stroke="#fff" stroke-width="0.8"/><path d="M2.7 7 H11.3 M3.4 4.8 H10.6 M3.4 9.2 H10.6" stroke="#fff" stroke-width="0.7"/></svg>
        yourwebsitehere.com
      </li>
      <li class="contact-item">
        <svg class="contact-icon" viewBox="0 0 14 14"><rect width="14" height="14" rx="2" fill="#27348b"/><path d="M7 11.5 Q3.8 7.8 3.8 5.8 A3.2 3.2 0 0 1 10.2 5.8 Q10.2 7.8 7 11.5Z" fill="#fff"/><circle cx="7" cy="5.8" r="1.2" fill="#27348b"/></svg>
        your address here
      </li>
    </ul>
    <div class="divider"></div>
    <div class="monogram">KM</div>
    <div class="social-row" aria-label="Social links">
      <span class="social-dot"></span>
      <span class="social-dot"></span>
      <span class="social-dot"></span>
      <span class="social-dot"></span>
    </div>
  </section>
</main>
</body>
</html>
```